PPC Landing Page For Technology Consultant

Looking for a high converting landing page for PPC and other Web Marketing traffic. Main objective is to complete a contact form on the main page (preferably at the top built into header image but open to ideas).

WORDPRESS ONLY. All Elements from Website (www.velntrabid.example) are available in adobe format)

Target Market(s)

IT Professionals in mid market and enterprise industries

Industry/Entity Type

It Service

Font styles to use
Sans Serif

Requirements
Must have
• Wordpress theme, customizable and re-usable. Will need help implementing the new site in our wordpress subdomain.
• Contact Form prominent and highlighted, as well as other call to actions (call, get a quote etc.)
Nice to have
• Scrolling logo list of our partners, or some other way to highlight to the our deep portfolio of providers (http://www.velntrabid.example/our-suppliers/), Products, Services etc.
• Some Testimonial section would be nice as well.

```html
<!DOCTYPE html>
<html lang="en">
<head>
<meta charset="utf-8">
<title>Velntrabid — Best Pricing Guaranteed</title>
<link href="https://fonts.googleapis.com/css2?family=Roboto+Condensed:wght@400;700&family=Roboto:wght@300;400;500;700&display=swap" rel="stylesheet">
<style>
:root{
  --navy:#16325c;
  --ink:#1b1f4a;
  --orange:#f7941d;
  --coral:#f2676a;
  --bg:#f7f7f7;
  --text:#5a5a66;
  --muted:#8a8a96;
  --partner:#9aa6bd;
  --line:#9aa3b3;
  --white:#ffffff;
}
*{margin:0;padding:0;box-sizing:border-box}
html,body{width:1200px;height:5042px;overflow:hidden;background:var(--bg)}
body{position:relative;font-family:"Roboto",sans-serif;color:var(--text)}
.abs{position:absolute}
.brand{font-family:"Roboto Condensed",sans-serif;font-weight:700;color:var(--orange);font-size:22px;letter-spacing:.5px}
.nav{top:52px;left:542px;display:flex;gap:38px;font-size:10px;letter-spacing:2.4px;color:var(--ink);font-weight:500}
.hero-title{left:170px;top:212px;font-family:"Roboto Condensed",sans-serif;font-weight:700;font-size:52px;color:var(--ink);letter-spacing:-.5px}
.hero-sub{left:172px;top:282px;font-size:21px;font-weight:500;color:var(--orange)}
.hero-copy{left:172px;top:383px;width:250px;font-size:12.5px;line-height:19px;color:var(--text);font-weight:300}
.pill{background:var(--orange);color:var(--white);font-weight:700;font-size:13px;border-radius:20px;text-align:center;letter-spacing:.5px}
.btn-save{left:172px;top:459px;width:112px;height:26px;line-height:26px}
.phone{left:172px;top:596px;font-size:11px;letter-spacing:1.5px;color:var(--ink);display:flex;align-items:center;gap:8px}
.quote-mark{font-family:Georgia,serif;font-size:150px;color:#d4d4d8;line-height:1}
.testimonial{left:262px;top:858px;width:680px;text-align:center;font-size:13.5px;line-height:34px;letter-spacing:.9px;color:var(--text);font-weight:300}
.author{left:400px;top:1128px;width:400px;text-align:center;color:var(--orange);font-size:14px;line-height:18px;letter-spacing:.5px}
.h2{font-weight:400;color:var(--ink)}
.more-title{left:690px;top:1350px;font-size:28px}
.more-sub{left:690px;top:1397px;width:300px;font-size:14px;line-height:19px;color:var(--orange);letter-spacing:.4px}
.more-copy{left:690px;top:1473px;width:265px;font-size:9px;line-height:13px;letter-spacing:.6px;color:var(--muted)}
.checks{left:690px;top:1543px;list-style:none;font-size:9.5px;letter-spacing:.8px;color:var(--muted)}
.checks li{height:24.6px;display:flex;align-items:center;gap:12px}
.checks li::before{content:"";width:6px;height:6px;border-radius:50%;background:#8cc63f}
.btn-quote{left:689px;top:1787px;width:113px;height:26px;line-height:26px;font-size:11px;letter-spacing:1px}
.navy-panel{background:var(--navy)}
.feature{width:270px;text-align:right}
.feature h3{font-weight:400;font-size:15px;color:var(--orange);letter-spacing:.5px;margin-bottom:12px}
.feature p{font-size:8.5px;line-height:13px;letter-spacing:.6px;color:var(--muted)}
.unbiased{left:738px;top:2152px;width:300px;font-size:29px;line-height:36px;color:var(--white);font-weight:400}
.partners-title{left:0;width:1200px;top:2628px;text-align:center;font-size:28px;color:var(--orange);font-weight:400}
.partner{width:200px;margin-left:-100px;text-align:center;font-size:25px;font-weight:500;color:var(--partner);letter-spacing:.3px}
.form-title{left:237px;top:3465px;font-size:19px;color:var(--ink)}
.field-label{left:237px;font-size:7px;letter-spacing:.5px;color:var(--muted)}
.field-line{left:237px;width:157px;height:1px;background:var(--line)}
.field-box{left:237px;width:229px;height:61px;border:1px solid var(--line);background:var(--white)}
.btn-send{left:237px;top:3888px;width:92px;height:20px;line-height:20px;background:var(--navy);color:var(--white);font-size:10px;font-weight:700;text-align:center;letter-spacing:1px}
.call-phone{left:689px;top:3473px;font-size:12px;color:var(--white);letter-spacing:.3px}
.call-title{left:626px;top:3527px;font-size:19px;color:var(--white)}
.call-copy{left:689px;width:275px;font-size:9.5px;line-height:13px;letter-spacing:.7px;color:#c8d1e0}
.btn-get{left:626px;top:3888px;width:91px;height:20px;line-height:20px;background:var(--white);color:var(--navy);font-size:10px;font-weight:700;text-align:center;letter-spacing:1px}
.portfolio-title{left:0;width:1200px;top:4156px;text-align:center;font-size:29px}
.svc-label{font-size:12.5px;line-height:16px;color:#5b6170}
.svc-label.right{text-align:right}
.footer{left:0;top:4828px;width:1200px;height:214px;background:var(--navy)}
.foot-col{top:4862px;width:200px}
.foot-col h4{font-size:14px;font-weight:500;color:var(--orange);margin-bottom:8px;letter-spacing:.4px}
.foot-col li{list-style:none;font-size:9.5px;line-height:13.3px;color:#c8d1e0;letter-spacing:.4px}
.foot-about{font-size:8.5px;line-height:13px;color:#c8d1e0;width:215px;letter-spacing:.3px}
.copyright{left:0;width:1200px;top:5008px;text-align:center;font-size:9.5px;color:#c8d1e0;letter-spacing:.5px}
</style>
</head>
<body>

<!-- Header -->
<div class="abs brand" style="left:172px;top:41px">VELNTRABID</div>
<nav class="abs nav"><span>SERVICES</span><span>SUPPLIERS</span><span>TESTIMONIALS</span><span>PARTNERSHIP</span><span>CONTACT US</span></nav>

<!-- Hero -->
<svg class="abs" style="left:168px;top:180px" width="1032" height="495" viewBox="0 0 1032 495" role="img" aria-label="Illustration of a business handshake, analytics dashboard, contract, coins and bar charts on a flowing orange path">
  <defs><linearGradient id="heroGrad" x1="0" y1="1" x2="1" y2="0"><stop offset="0" stop-color="#f2676a"/><stop offset="1" stop-color="#f7b36a"/></linearGradient></defs>
  <path d="M0,491 C250,470 520,470 580,380 C640,290 470,270 530,210 C600,140 820,170 1032,140 L1032,491 Z" fill="url(#heroGrad)"/>
</svg>
<h1 class="abs hero-title">Best Pricing Guaranteed</h1>
<div class="abs hero-sub">Global Footprint With 250+ Suppliers</div>
<p class="abs hero-copy">Leverage better-than-direct pricing and post-sales support from nearly every ISP, VoIP and Cloud Provider.</p>
<div class="abs pill btn-save">SAVE 70%</div>
<div class="abs phone">
  <svg width="14" height="14" viewBox="0 0 14 14"><circle cx="7" cy="7" r="7" fill="#f7941d"/><path d="M4.5 4c.5-.5 1-.4 1.3.1l.5.9c.2.4 0 .7-.3.9-.3.2-.3.5 0 .9.4.6.8 1 1.4 1.4.4.3.7.3.9 0 .2-.3.5-.5.9-.3l.9.5c.5.3.6.8.1 1.3-1.4 1.2-4.4-1-5.7-3.7C4 5.3 4 4.5 4.5 4z" fill="#fff"/></svg>
  1-888-555-0142
</div>

<!-- Testimonial -->
<div class="abs quote-mark" style="left:182px;top:795px">“</div>
<p class="abs testimonial">I’ve recently been working with Velntrabid to assist with providing communications services to client offices in the US. Their level of customer service has been excellent, with rapid responses to questions &amp; requests. They have done a great job of providing numerous options, and have been very patient and helpful when I ’ve had questions about services, terminology, etc. Having a broker that knows the market, the providers, and the products has been a godsend, and having all the options priced out along with recommendations makes the whole process smooth</p>
<div class="abs quote-mark" style="left:860px;top:1040px">”</div>
<div class="abs author">- Dana Whitlock, IT Manager<br>International MSP</div>

<!-- More than best price -->
<svg class="abs" style="left:166px;top:1370px" width="490" height="333" role="img" aria-label="Isometric illustration of consultants working with devices, charts and data panels">
  <defs><linearGradient id="isoGrad" x1="0" y1="0" x2="1" y2="1"><stop offset="0" stop-color="#e4ecf7"/><stop offset="1" stop-color="#d3e1f2"/></linearGradient></defs>
  <path d="M20,180 L245,40 L470,180 L245,320 Z" fill="url(#isoGrad)"/>
</svg>
<h2 class="abs h2 more-title">More Than “Best Price”</h2>
<div class="abs more-sub">World-class post-sales support and lifecycle management.</div>
<p class="abs more-copy">Our clients' success matters to us – a lot. Take advantage of "white glove" service, unique, deep escalation paths and insanely responsive post-sales support from day 1.</p>
<ul class="abs checks">
  <li>Consulting &amp; Solution Recommendations</li>
  <li>Plan &amp; Design</li>
  <li>Contract Negotiations</li>
  <li>Project Management</li>
  <li>Post Install Support Escalations</li>
  <li>On Going Supplier Review Check Ins</li>
  <li>Renewal Negotiations</li>
</ul>
<div class="abs pill btn-quote">GET QUOTE</div>

<!-- Features -->
<div class="abs feature" style="left:243px;top:2026px"><h3>Trusted Advisor</h3><p>Take advantage of our longstanding relationships with hundreds of ISP, VoIP and Cloud providers for better-than-direct pricing and enhanced post-sales support/escalation channels</p></div>
<div class="abs feature" style="left:243px;top:2195px"><h3>Global Reach</h3><p>Deep product reach from hundreds of world-class service providers gives you a competitive edge on a global scale</p></div>
<div class="abs feature" style="left:243px;top:2332px"><h3>Right-Fit Technology</h3><p>We've seen it all. Our expertise and experience span geographies, suppliers, industries, and verticals which means you'll get unbiased recommendations designed to solve your problems.</p></div>
<svg class="abs" style="left:563px;top:2026px" width="80" height="80" role="img" aria-label="Advisor icon"><circle cx="40" cy="40" r="39" fill="#2bb3a0"/></svg>
<svg class="abs" style="left:563px;top:2192px" width="80" height="80" role="img" aria-label="Globe icon"><circle cx="40" cy="40" r="39" fill="#2bb3a0"/></svg>
<svg class="abs" style="left:563px;top:2349px" width="80" height="80" role="img" aria-label="Hand holding cards icon"><circle cx="40" cy="40" r="39" fill="#2bb3a0"/></svg>
<div class="abs navy-panel" style="left:706px;top:2016px;width:494px;height:421px"></div>
<div class="abs unbiased">Unbiased, Free Consulting &amp; Design from Industry Veterans</div>

<!-- Partners -->
<h2 class="abs partners-title">Our Partners</h2>
<div class="abs partner" style="left:82px;top:2747px">Arkvale</div>
<div class="abs partner" style="left:313px;top:2747px">Appton</div>
<div class="abs partner" style="left:552px;top:2747px">Airewell</div>
<div class="abs partner" style="left:763px;top:2747px">Bigridge</div>
<div class="abs partner" style="left:953px;top:2747px">Atlantel</div>
<div class="abs partner" style="left:1120px;top:2747px">Transvane</div>
<div class="abs partner" style="left:82px;top:2845px">Centrix</div>
<div class="abs partner" style="left:313px;top:2845px">Callspire</div>
<div class="abs partner" style="left:552px;top:2845px">Accessly</div>
<div class="abs partner" style="left:763px;top:2845px">Expenor</div>
<div class="abs partner" style="left:953px;top:2845px">Exodo</div>
<div class="abs partner" style="left:1110px;top:2845px">Coltra</div>
<div class="abs partner" style="left:82px;top:2941px">Impella</div>
<div class="abs partner" style="left:313px;top:2941px">Corelane</div>
<div class="abs partner" style="left:552px;top:2941px">Fiberpoint</div>
<div class="abs partner" style="left:763px;top:2941px">Palmora</div>
<div class="abs partner" style="left:953px;top:2941px">Peakline</div>
<div class="abs partner" style="left:1110px;top:2941px">Internova</div>
<div class="abs partner" style="left:82px;top:3039px">Megarail</div>
<div class="abs partner" style="left:313px;top:3039px">Grandeo</div>
<div class="abs partner" style="left:552px;top:3039px">Lightreach</div>
<div class="abs partner" style="left:763px;top:3039px">Mediastream</div>
<div class="abs partner" style="left:953px;top:3039px">Inetra</div>
<div class="abs partner" style="left:1110px;top:3039px">Firstwave</div>
<div class="abs partner" style="left:82px;top:3143px">Nettora</div>
<div class="abs partner" style="left:313px;top:3143px">Globalspan</div>
<div class="abs partner" style="left:552px;top:3143px">Maserly</div>
<div class="abs partner" style="left:763px;top:3143px">Suddenvale</div>
<div class="abs partner" style="left:953px;top:3143px">Ozenta</div>
<div class="abs partner" style="left:1110px;top:3143px">Spirex</div>

<!-- Contact -->
<div class="abs navy-panel" style="left:566px;top:3395px;width:461px;height:568px"></div>
<h2 class="abs h2 form-title">Write to Us</h2>
<div class="abs field-label" style="top:3509px">Business Name</div><div class="abs field-line" style="top:3523px"></div>
<div class="abs field-label" style="top:3548px">Contact Name</div><div class="abs field-line" style="top:3562px"></div>
<div class="abs field-label" style="top:3589px">Email</div><div class="abs field-line" style="top:3603px"></div>
<div class="abs field-label" style="top:3630px">Phone</div><div class="abs field-line" style="top:3644px"></div>
<div class="abs field-label" style="top:3672px">I am looking for</div><div class="abs field-box" style="top:3689px"></div>
<div class="abs field-label" style="top:3762px">Service Location</div><div class="abs field-box" style="top:3779px"></div>
<div class="abs btn-send">SEND</div>
<div class="abs call-phone">1-888-555-0142</div>
<div class="abs call-title">Call Us</div>
<p class="abs call-copy" style="top:3597px">For immediate service, or fill out the form and a Technology Services expert will be in touch right away.</p>
<p class="abs call-copy" style="top:3675px">We pride ourselves on the trust we've earned from thousands of our business customers over the years. We are dedicated to solving telecom problems cost effectively across your entire organization.</p>
<p class="abs call-copy" style="top:3793px">We do the legwork. You save up to 70% on connectivity, voice and cloud.</p>
<div class="abs btn-get">GET QUOTE</div>

<!-- Portfolio -->
<h2 class="abs h2 portfolio-title">Deep Product Portfolio</h2>
<svg class="abs" style="left:147px;top:4420px" width="910" height="280" role="img" aria-label="World map showing global service coverage">
  <defs><linearGradient id="mapGrad" x1="0" y1="0" x2="1" y2="0"><stop offset="0" stop-color="#1d3b6a"/><stop offset="1" stop-color="#2a4c80"/></linearGradient></defs>
  <rect x="0" y="0" width="910" height="280" rx="40" fill="url(#mapGrad)"/>
</svg>
<svg class="abs" style="left:0;top:4200px" width="1200" height="320" role="img" aria-label="Service category icons">
  <circle cx="587" cy="70" r="35" fill="#f05a28"/>
  <circle cx="476" cy="125" r="35" fill="#f7b21d"/>
  <circle cx="685" cy="111" r="25" fill="#2b8fc7"/>
  <circle cx="828" cy="100" r="23" fill="#1d3b6a"/>
  <circle cx="288" cy="233" r="18" fill="#f5c48a"/>
  <circle cx="450" cy="209" r="23" fill="#8cc63f"/>
  <circle cx="636" cy="190" r="25" fill="#6fa8dc"/>
  <circle cx="826" cy="246" r="37" fill="#8cc63f"/>
  <circle cx="943" cy="222" r="27" fill="#f05a28"/>
  <circle cx="524" cy="277" r="23" fill="#f7b21d"/>
</svg>
<div class="abs svc-label" style="left:632px;top:4237px">SIP Trunking</div>
<div class="abs svc-label right" style="left:248px;top:4270px;width:200px">Telecommunications<br>Consulting</div>
<div class="abs svc-label" style="left:720px;top:4288px">Global<br>Private<br>Connectivity</div>
<div class="abs svc-label" style="left:861px;top:4283px">Advanced 24/7<br>Monitoring</div>
<div class="abs svc-label" style="left:268px;top:4390px">MPLS</div>
<div class="abs svc-label" style="left:481px;top:4368px">Dedicated<br>Internet Access</div>
<div class="abs svc-label" style="left:669px;top:4371px">Hosted<br>Voice</div>
<div class="abs svc-label" style="left:778px;top:4371px">Unified<br>Communications</div>
<div class="abs svc-label" style="left:939px;top:4371px">Failover</div>
<div class="abs svc-label right" style="left:372px;top:4466px;width:120px">Private<br>Networks</div>

<!-- Footer -->
<footer class="abs footer"></footer>
<div class="abs foot-col" style="left:172px"><h4>Read More</h4><ul><li>Technology Solutions</li><li>Suppliers</li><li>Partnership</li><li>Testimonials</li><li>Request a Quote</li><li>Contact Us</li></ul></div>
<div class="abs foot-col" style="left:409px"><h4>Contact Us</h4><ul><li>team@velntrabid.example</li><li>1-888-555-0142</li></ul></div>
<div class="abs foot-col" style="left:646px"><h4>Quick Links</h4><ul><li>About Us</li><li>How It Works</li><li>FAQ</li><li>Blog</li><li>Terms &amp; Conditions</li><li>Privacy Policy</li></ul></div>
<div class="abs foot-col" style="left:861px;width:230px"><div class="brand" style="font-size:15px;margin-bottom:8px">VELNTRABID</div><p class="foot-about">Whatever your technology needs may be, let the experts at Velntrabid help you navigate and negotiate the most cost effective solution(s) from over 250 ISP, VoIP and cloud providers around the world — all with better-than-direct pricing and post-sales support/escalation channels.</p></div>
<div class="abs copyright">Copyright © 2020 VELNTRABID</div>

</body>
</html>
```